Networking card

I just need a simple design with the following information:
Milan Dorsey
415.608.2931
mdorsey083651@quillpost.example

I would like to have a white background with blue text like in this sample: https://lumacardstudio.example/business-card-527306/

```html
<!DOCTYPE html>
<html lang="en">
<head>
<meta charset="utf-8">
<title>Milan Dorsey – Business Card</title>
<link rel="stylesheet" href="https://fonts.googleapis.com/css2?family=Saira+Semi+Condensed:wght@400;700&display=swap">
<style>
  :root {
    --page-bg: #e4e4e4;
    --card-bg: #ffffff;
    --ink: #1b4a6b;
    --rule: #8a8a8a;
  }
  html, body {
    margin: 0;
    padding: 0;
    width: 1200px;
    height: 1200px;
    overflow: hidden;
    background: var(--page-bg);
  }
  .business-card {
    position: absolute;
    left: 100px;
    top: 314px;
    width: 1000px;
    height: 571px;
    background: var(--card-bg);
    box-shadow: 0 4px 14px rgba(0,0,0,0.12);
    font-family: "Saira Semi Condensed", sans-serif;
    color: var(--ink);
  }
  .identity {
    position: absolute;
    left: 134px;
    top: 158px;
  }
  .person-name {
    margin: 0;
    font-size: 46px;
    font-weight: 700;
    letter-spacing: 1px;
    line-height: 1;
    text-transform: uppercase;
  }
  .person-title {
    margin: 6px 0 0;
    font-size: 28px;
    font-weight: 400;
    line-height: 1.1;
    letter-spacing: 0.5px;
  }
  .divider {
    position: absolute;
    left: 134px;
    top: 273px;
    width: 96px;
    height: 2px;
    background: linear-gradient(90deg, rgba(138,138,138,0.3), var(--rule), rgba(138,138,138,0.3));
  }
  .contact-list {
    position: absolute;
    left: 130px;
    top: 316px;
    margin: 0;
    padding: 0;
    list-style: none;
  }
  .contact-item {
    display: flex;
    align-items: center;
    height: 40px;
    font-size: 31px;
    font-weight: 400;
    letter-spacing: 0.6px;
  }
  .contact-icon {
    width: 37px;
    height: 37px;
    margin-right: 14px;
    flex: none;
  }
</style>
</head>
<body>
  <main class="business-card">
    <div class="identity">
      <h1 class="person-name">Milan Dorsey</h1>
      <p class="person-title">President</p>
    </div>
    <div class="divider"></div>
    <ul class="contact-list">
      <li class="contact-item">
        <svg class="contact-icon" viewBox="0 0 36 36" aria-hidden="true">
          <circle cx="18" cy="18" r="18" fill="var(--ink)"/>
          <path d="M12.2 9.5c.6-.5 1.5-.4 2 .2l2.2 3c.4.6.3 1.4-.2 1.9l-1.3 1.1c.9 2 2.4 3.6 4.4 4.6l1.1-1.3c.5-.5 1.3-.6 1.9-.2l3 2.1c.6.4.8 1.3.3 1.9l-1.3 1.8c-.7.9-1.9 1.3-3 .9-5.2-1.8-9.2-5.8-11-11-.4-1.1 0-2.3.9-3z" fill="#fff"/>
        </svg>
        <span class="contact-text">415.608.2931</span>
      </li>
      <li class="contact-item">
        <svg class="contact-icon" viewBox="0 0 36 36" aria-hidden="true">
          <circle cx="18" cy="18" r="18" fill="var(--ink)"/>
          <rect x="9" y="12" width="18" height="12" rx="1" fill="none" stroke="#fff" stroke-width="1.8"/>
          <path d="M9.5 12.8 18 19.3l8.5-6.5M9.5 23.3l6-5M26.5 23.3l-6-5" fill="none" stroke="#fff" stroke-width="1.6"/>
        </svg>
        <span class="contact-text">mdorsey083651@quillpost.example</span>
      </li>
    </ul>
  </main>
</body>
</html>
```